Renata Quisby

Luxury And Style -

Black - White & Gold

Target Market(s)

Fashion

Industry/Entity Type

Fashion

Requirements
Must have
• High-End
Nice to have
• We will Print on Silk Paper

```html
<!DOCTYPE html>
<html lang="en">
<head>
<meta charset="utf-8">
<title>Renata Quisby Letterhead</title>
<link href="https://fonts.googleapis.com/css2?family=Lato:wght@400;700&family=Marcellus&display=swap" rel="stylesheet">
<style>
  :root {
    --backdrop: #c9c9c9;
    --paper: #ffffff;
    --paper-shade: #efefef;
    --band: #ebe5e1;
    --band-warm: #f1e9e4;
    --ink: #1e1e1e;
    --ink-soft: #555555;
    --rule: #6f6f6f;
    --block: #2b2b2b;
    --signature-fill: #e4e1df;
  }
  * { box-sizing: border-box; margin: 0; padding: 0; }
  html, body { width: 1200px; height: 932px; overflow: hidden; }
  body { background: var(--backdrop); font-family: "Lato", sans-serif; color: var(--ink); }

  .letterhead {
    position: absolute; left: 260px; top: 26px; width: 680px; height: 880px;
    background: radial-gradient(circle at 60% 45%, var(--paper) 0%, var(--paper-shade) 75%);
    box-shadow: 0 6px 18px rgba(0,0,0,0.18);
    overflow: hidden;
  }
  .side-band {
    position: absolute; left: 0; top: 0; width: 250px; height: 100%;
    background: linear-gradient(180deg, var(--band) 0%, var(--band-warm) 55%, var(--band) 100%);
  }
  .brand-block {
    position: absolute; left: 78px; top: 150px; width: 62px; height: 32px; background: var(--block);
  }
  .brand-name {
    position: absolute; left: 0; width: 250px; top: 212px; text-align: center;
    font-size: 17px; font-weight: 400; letter-spacing: 3px; text-transform: uppercase; color: var(--ink);
  }
  .brand-tagline {
    position: absolute; left: 0; width: 250px; top: 238px; text-align: center;
    font-family: "Marcellus", serif; font-size: 8px; letter-spacing: 1.5px; text-transform: uppercase; color: var(--ink-soft);
  }
  .side-rule { position: absolute; left: 40px; width: 170px; top: 262px; height: 1px; background: var(--rule); }
  .contact {
    position: absolute; left: 52px; top: 282px; font-family: "Marcellus", serif; font-size: 10.5px;
    line-height: 17px; color: var(--ink-soft); list-style: none;
  }
  .contact li { display: flex; align-items: center; gap: 6px; }
  .contact svg { width: 9px; height: 9px; fill: var(--ink-soft); }
  .side-rule-bottom { position: absolute; left: 60px; width: 130px; top: 830px; height: 1px; background: var(--rule); }

  .letter {
    position: absolute; left: 300px; top: 118px; width: 340px;
    display: flex; flex-direction: column;
  }
  .top-rule { width: 90px; height: 1px; background: var(--rule); }
  .recipient { margin-top: 32px; }
  .recipient-name { font-size: 13px; font-weight: 700; line-height: 16px; }
  .recipient-role, .sender-role { font-size: 9px; line-height: 12px; color: var(--ink-soft); }
  .body-copy { margin-top: 26px; font-size: 9px; line-height: 14.5px; color: var(--ink-soft); }
  .body-copy p + p { margin-top: 22px; }
  .sender { margin-top: 26px; }
  .sender-name { font-size: 13px; font-weight: 700; line-height: 16px; color: #444; }
  .signature {
    margin: 8px 0 0 10px; width: 150px; height: 38px;
    background: var(--signature-fill); border-radius: 3px;
  }
  .bottom-rule { margin-top: 26px; width: 340px; height: 1px; background: var(--rule); }
</style>
</head>
<body>
  <main class="letterhead">
    <aside class="side-band">
      <div class="brand-block"></div>
      <div class="brand-name">Renata Quisby</div>
      <div class="brand-tagline">Luxury and Style</div>
      <div class="side-rule"></div>
      <ul class="contact">
        <li>48 Orchard Lane</li>
        <li>Westbrook, NY 10452</li>
        <li><svg viewBox="0 0 10 10"><path d="M2 1h2l1 2-1.2 1a5 5 0 0 0 2.2 2.2L7 5l2 1v2a1 1 0 0 1-1 1A7 7 0 0 1 1 2a1 1 0 0 1 1-1z"/></svg>+1 555 014 2870</li>
        <li><svg viewBox="0 0 10 10"><path d="M0 2h10v6H0z"/><path d="M0 2l5 3.5L10 2" fill="none" stroke="#fff" stroke-width=".8"/></svg>info@renataquisby.com</li>
        <li><svg viewBox="0 0 10 10"><circle cx="5" cy="5" r="4.5"/></svg>www.renataquisby.com</li>
      </ul>
      <div class="side-rule-bottom"></div>
    </aside>

    <section class="letter">
      <div class="top-rule"></div>
      <div class="recipient">
        <div class="recipient-name">Dear. Daniel Morrow</div>
        <div class="recipient-role">Chief Director</div>
      </div>
      <div class="body-copy">
        <p>Lorem ipsum dolor sit amet, consectetur adipiscing elit, sed do eiusmod tempor incididunt ut labore et dolore magna aliqua. Sollicitudin ac orci phasellus egestas tellus rutrum tellus. Euismod elementum nisi quis eleifend quam adipiscing vitae proin sagittis. Egestas sed tempus urna et pharetra pharetra. Quis blandit turpis cursus in hac habitasse. Sed velit dignissim sodales ut eu. Ac auctor augue mauris augue neque. In arcu cursus euismod quis viverra nibh cras pulvinar mattis. Libero justo laoreet sit amet. Felis eget nunc lobortis mattis aliquam faucibus purus in. Pulvinar etiam non quam lacus suspendisse faucibus. Odio tempor orci dapibus ultrices. Velit dignissim sodales ut eu sem integer vitae justo. Fermentum et sollicitudin ac orci phasellus egestas. Pharetra vel turpis nunc eget lorem dolor sed. Sed turpis tincidunt id aliquet risus feugiat in ante. Mus mauris vitae ultricies leo integer malesuada nunc vel. Rhoncus urna neque viverra justo nec ultrices dui. Ut placerat orci nulla pellentesque dignissim enim sit amet.</p>
        <p>Bibendum arcu vitae elementum curabitur vitae nunc. Nunc pulvinar sapien et ligula ullamcorper malesuada. At elementum eu facilisis sed. Erat pellentesque adipiscing commodo elit at imperdiet dui accumsan sit. Nunc scelerisque viverra mauris in aliquam sem fringilla. In vitae turpis massa sed. Volutpat ac tincidunt vitae semper quis lectus nulla at. Massa placerat duis ultricies lacus sed turpis. Dui vivamus arcu felis bibendum ut tristique et egestas. Blandit aliquam etiam erat velit scelerisque in dictum non consectetur. Id neque aliquam vestibulum morbi blandit cursus risus at. Sed egestas egestas fringilla phasellus faucibus scelerisque eleifend donec. Ornare quam viverra orci sagittis eu volutpat odio facilisis. Volutpat sed cras ornare arcu dui vivamus arcu. Interdum consectetur libero id faucibus nisl.</p>
        <p>Viverra mauris in aliquam sem. Mattis molestie a iaculis at erat pellentesque adipiscing commodo elit. Sit amet volutpat consequat mauris nunc. Aliquam nulla facilisi cras fermentum. Sed turpis tincidunt id aliquet risus feugiat. Augue neque gravida in fermentum et sollicitudin ac orci.</p>
      </div>
      <div class="sender">
        <div class="sender-name">Owen Kessler</div>
        <div class="sender-role">Chief Director</div>
      </div>
      <div class="signature" role="img" aria-label="Handwritten signature of Owen Kessler"></div>
      <div class="bottom-rule"></div>
    </section>
  </main>
</body>
</html>
```